Tarn - Stationary Design/Layout

We are a well established clothing design and manufacturing company (Tarn Sourcing) based in London UK, with our own factory in Bangladesh, supplying to many fashion retailers and brands. Our factory has very high environmental and ethical standards with people at its heart. Our quality of garments are second to none.
Our new logo has been proudly developed by the Pixel Guild community last month, we are now in the second phase and need the layout designed for our letterheads, double sided business cards, compliment slip and clothing ticket. Feel as creative as you like, but make sure it looks great!!
***The Logo - the logo design and colour is set and should NOT be changed and stay on a dark grey backround. The logo artwork to use is attached.
***Details to use for the business card:
Dorian Pelham
Direct Line: 020 7946 0158
dorian@tarnsourcing-example.com
Tarn Sourching Ltd.
57 - 59 Hollin Row
Harlow Vale . Milbury
NW9 4QT
Switchboard: 020 7946 0274
Fax: 020 7946 0274
www.tarnsourcing-example.co.uk
***Details to use for the letterhead and compliment slip:
Tarn Sourching Ltd.
57 - 59 Hollin Row
Harlow Vale . Milbury
NW9 4QT
Fax: 020 7946 0274
www.tarnsourcing-example.co.uk
***Details for Swing Ticket:
Size: 12cm height by 5.5cm width
One side need to have just the logo without the 'Sourcing', on the other it needs to stay blank

```html
<!DOCTYPE html>
<html lang="en">
<head>
<meta charset="utf-8">
<title>Tarn Sourcing Letterhead</title>
<link rel="stylesheet" href="https://fonts.googleapis.com/css2?family=Jost:wght@400;600&display=swap">
<style>
  :root {
    --charcoal: #2a3134;
    --mint: #b4fbe5;
    --mint-faint: #effcf8;
    --paper: #ffffff;
    --ink: #2a3134;
  }
  html, body {
    margin: 0;
    padding: 0;
    width: 849px;
    height: 1200px;
    overflow: hidden;
    background: var(--charcoal);
  }
  .letterhead {
    position: relative;
    width: 849px;
    height: 1200px;
    background: var(--charcoal);
    font-family: "Jost", "Century Gothic", sans-serif;
    color: var(--ink);
  }
  .frame {
    position: absolute;
    left: 40px;
    top: 40px;
    width: 769px;
    height: 1120px;
    background: var(--mint);
  }
  .sheet {
    position: absolute;
    left: 53px;
    top: 53px;
    width: 744px;
    height: 1093px;
    background: var(--paper);
  }
  .brand-block {
    position: absolute;
    left: 560px;
    top: 84px;
    width: 204px;
    height: 68px;
    background: var(--charcoal);
    display: flex;
    align-items: center;
    justify-content: center;
  }
  .brand-name {
    color: var(--mint);
    font-weight: 400;
    font-size: 26px;
    letter-spacing: 1px;
    white-space: nowrap;
  }
  .contact {
    position: absolute;
    left: 560px;
    top: 166px;
    font-size: 13px;
    line-height: 20px;
    font-style: normal;
    margin: 0;
  }
  .contact p { margin: 0; white-space: nowrap; }
  .contact .company { font-weight: 600; }
  .contact .label { font-weight: 600; }
  .contact .gap { margin-top: 19px; }
  .contact .dot {
    color: var(--mint);
    padding: 0 4px;
  }
  .watermark {
    position: absolute;
    color: var(--mint-faint);
    font-weight: 400;
    font-size: 56px;
    line-height: 1;
    letter-spacing: 12px;
    text-transform: uppercase;
  }
  .watermark--left { left: 84px; top: 1040px; }
  .watermark--right { left: 566px; top: 1034px; }
</style>
</head>
<body>
  <main class="letterhead">
    <div class="frame"></div>
    <div class="sheet"></div>

    <div class="brand-block">
      <span class="brand-name">Tarn Sourcing</span>
    </div>

    <address class="contact">
      <p class="company">Tarn Sourching Ltd.</p>
      <p>57 - 59 Hollin Row</p>
      <p>Harlow Vale<span class="dot">&bull;</span>Milbury<span class="dot">&bull;</span>NW9 4QT</p>
      <p class="gap"><span class="label">Switchboard:</span> 020 7946 0274</p>
      <p><span class="label">Fax:</span> 020 7946 0274</p>
      <p>www.tarnsourcing-example.co.uk</p>
    </address>

    <div class="watermark watermark--left" aria-hidden="true">Tarn</div>
    <div class="watermark watermark--right" aria-hidden="true">Tarn</div>
  </main>
</body>
</html>
```